Redesign Home Page

We need a new home page with a white background. Our company provides singing instruction to students world wide, both in person and on line. We're looking for a very clean and open design with maximum white space. The main goal of the page will be to get users to sign up for our mailing list. The current site is www.kelvarsong.com. I think the new page can be a long page (scrolll down is ok), to allow for more white space while still using the text from the current page.
Updates

Project Deadline Extended
Reason: Hello to all Designers, I apologize for not giving feedback this weekend. We went out of town for the Memorial Day holiday and I had no internet. I will be extending the deadline to Thursday. -Marcus

Target Market(s)

Singers of all ages and abilities, especially beginners.

Industry/Entity Type

It Company

Requirements
Must have
• 1. A white background
2. Lots of open space
3. An email sign up form on the top right that reads:
a. “Improve Your Singing Now.
b. Sign up for our Free Video Series: Tone Quest
4. Testimonails: found on https://www.kelvarsong.com/tone-ascent
5. My logo with the piano
6. My photo
7. Learn about our Lessons in:
a. San Francisco
b. Alameda
8. On Line Programs:
a. Tone Ascent
b. Wavlo Lessons

Nice to have
• Link to current student page: http://kelvarsong.com/what-students-say/students2
Pictures of singers
Video box: Use Marcus_Example
Should not have
• See "KelvarSong Redesign" file for more details.

```html
<!DOCTYPE html>
<html lang="en">
<head>
<meta charset="utf-8">
<title>Marcus Hale School of Voice</title>
<link href="https://fonts.googleapis.com/css2?family=Ubuntu:wght@300;400;500&family=Open+Sans:ital,wght@0,400;0,600;0,700;1,400&display=swap" rel="stylesheet">
<style>
:root{
  --blue:#1b96d4;
  --blue-light:#3fb3e8;
  --blue-dark:#1479b3;
  --orange:#f08a12;
  --text:#6a6a6a;
  --text-dark:#444;
  --rule:#e2e2e2;
  --band:#efefee;
  --footer:#2b2b2b;
  --white:#fff;
}
*{box-sizing:border-box;margin:0;padding:0}
html,body{width:1200px;height:3306px;overflow:hidden;background:var(--white)}
body{position:relative;font-family:"Open Sans",Arial,sans-serif;color:var(--text)}
.abs{position:absolute}
h2{font-family:"Ubuntu",Arial,sans-serif;font-weight:400;color:var(--blue);font-size:31px;line-height:1.2}
p.copy{font-size:13.5px;line-height:30px;color:var(--text)}
.btn{position:absolute;display:flex;align-items:center;justify-content:center;background:var(--blue);color:var(--white);font-size:16px;border:2px solid var(--white);box-shadow:0 0 0 2px var(--blue);text-decoration:none}
.media{position:absolute}

/* header */
.brand{left:87px;top:50px;display:flex;align-items:center;gap:16px}
.brand-mark{width:86px;height:86px;background:var(--blue)}
.brand-name{font-family:"Ubuntu",Arial,sans-serif;font-weight:400;color:var(--blue-dark);font-size:42px;line-height:1}
.brand-name span{display:block;font-size:23px;margin-top:6px}
.account{left:835px;top:88px;font-size:15px;color:var(--text-dark)}
.signin{left:997px;top:74px;width:111px;height:42px;background:var(--blue);color:var(--white);font-size:16px;display:flex;align-items:center;justify-content:center;gap:10px}
.signin svg{width:10px;height:6px}

/* nav */
.nav{left:0;top:173px;width:1200px;height:55px;background:linear-gradient(#3ab2ea,#1e98d6);display:flex;padding-left:87px}
.nav a{display:flex;align-items:center;justify-content:center;color:var(--white);font-size:13px;font-weight:700;text-decoration:none;border-right:1px solid rgba(255,255,255,.35);letter-spacing:.2px}
.nav a.current{background:var(--blue-dark)}

/* hero */
.hero{left:0;top:228px;width:1200px;height:430px;background:linear-gradient(180deg,#dfe3e6 0%,#c9ced2 55%,#e4e6e8 100%)}
.hero-photo{left:200px;top:45px;width:250px;height:385px;background:linear-gradient(160deg,#6b4a3a,#3d7b4a 70%,#2f6a3f)}
.signup-title{left:653px;top:96px;font-size:31px}
.field{position:absolute;left:653px;width:416px;height:42px;background:var(--white);border:1px solid #d8d8d8;font-size:13px;color:#555;display:flex;align-items:center;padding-left:14px}
.start{left:915px;top:296px;width:154px;height:47px;background:var(--orange);color:var(--white);font-size:15px;display:flex;align-items:center;justify-content:center;letter-spacing:.3px}

.intro{left:87px;top:742px;width:1026px;text-align:center;font-size:14.5px;line-height:30px;color:var(--text)}

.rule{position:absolute;left:87px;width:1026px;height:1px;background:var(--rule)}

.consult{left:0;top:1954px;width:1200px;height:354px;background:var(--band)}
.testimonials{left:0;top:2734px;width:1200px;height:450px;background:linear-gradient(180deg,#ececec,#f6f6f6 50%,#e9e9e9)}
.testimonials h2{position:absolute;left:0;top:60px;width:1200px;text-align:center;font-size:34px}
.avatar{left:532px;top:111px;width:136px;height:136px;border-radius:50%;border:4px solid var(--white);background:linear-gradient(#c9a27e,#8c5d3e)}
.quote{left:200px;top:283px;width:800px;text-align:center;font-style:italic;font-size:15.5px;line-height:33px;color:#555}
.cite{left:800px;top:349px;width:290px;text-align:right;font-size:14px;font-weight:600;color:#555}
.dots{left:563px;top:400px;display:flex;gap:4px}
.dots i{width:13px;height:13px;border-radius:50%;background:#d4d4d4;border:1px solid #bbb}
.dots i.on{background:#999}

.footer{left:0;top:3184px;width:1200px;height:122px;background:var(--footer);color:var(--white);font-size:13px}
.footer .links{position:absolute;left:105px;top:36px}
.footer .legal{position:absolute;left:105px;top:70px}
.social{position:absolute;left:903px;top:45px;display:flex;gap:17px}
.social i{width:33px;height:33px;background:#555}
</style>
</head>
<body>

<header>
  <div class="abs brand">
    <div class="brand-mark"></div>
    <div class="brand-name">Marcus Hale<span>School of Voice</span></div>
  </div>
  <div class="abs account">Have an Account?</div>
  <a class="abs signin">Sign In
    <svg viewBox="0 0 10 6"><path d="M0 0h10L5 6z" fill="#fff"/></svg>
  </a>
</header>

<nav class="abs nav">
  <a class="current" style="width:99px">HOME</a>
  <a style="width:202px">VOICE LESSONS</a>
  <a style="width:226px">WHAT STUDENTS SAY</a>
  <a style="width:242px">MEET THE INSTRUCTORS</a>
  <a style="width:257px;border-right:none">TONE ASCENT</a>
</nav>

<section class="abs hero">
  <div class="abs hero-photo" role="img" aria-label="Photo of a young woman singing with headphones"></div>
  <h2 class="abs signup-title">Sign Up For Our Free Video Series</h2>
  <div class="field" style="top:180px">Name</div>
  <div class="field" style="top:237px">Email</div>
  <div class="abs start">GET STARTED</div>
</section>

<p class="abs intro">The Marcus Hale School of Voice offers state of the art voice instruction in San Francisco, Alameda, and on line. We love working with beginners and professionals, so whether you're just starting to explore singing or are an experienced preforming vocalist looking to perfect your singing technique, we can help.</p>

<section>
  <div class="media" style="left:87px;top:898px;width:336px;height:218px;background:linear-gradient(#8fbde6,#b8cfe0 45%,#2e5f8a 70%,#1d3f5e)" role="img" aria-label="Photo of a tugboat on the bay with the city skyline"></div>
  <h2 class="abs" style="left:490px;top:898px">Alameda</h2>
  <p class="abs copy" style="left:490px;top:943px;width:622px">This venue has a beautiful private studio equipped with a digital recording and video production capabilities. We offer private one on one voice lessons and producing. Whether you're just starting out and learning the basics or seasoned professional preparing for your next release, Marcus is available to help you.</p>
  <a class="btn" style="left:490px;top:1069px;width:158px;height:42px">Learn More</a>
</section>

<div class="rule" style="top:1192px"></div>

<section>
  <h2 class="abs" style="left:87px;top:1255px">San Francisco</h2>
  <p class="abs copy" style="left:87px;top:1298px;width:640px">Located downtown near the Corvane Hall, the studio is equipped with an Aldmark grand piano and all lessons are recorded onto CD (no charge). You can park at the Brannick Street Garage or take the Harbor Line to the Harlow Street Station. The studio is just a short walk from there. Our instructor Elena is an experienced vocalist and actor, and she is a delight to work with.</p>
  <a class="btn" style="left:87px;top:1427px;width:158px;height:42px">Learn More</a>
  <div class="media" style="left:774px;top:1259px;width:337px;height:218px;background:linear-gradient(#1a2748,#3b3a5e 45%,#c8793a 75%,#2a2a3a)" role="img" aria-label="Night photo of a suspension bridge and city lights"></div>
</section>

<div class="rule" style="top:1561px"></div>

<section>
  <div class="media" style="left:87px;top:1608px;width:383px;height:285px;background:linear-gradient(180deg,#fafafa,#e9eef3 40%,#4a6a9a 75%,#f4f4f4)" role="img" aria-label="Photo of a smiling student with headphones lying in front of a laptop"></div>
  <svg class="abs" style="left:589px;top:1641px" width="26" height="26" viewBox="0 0 26 26"><circle cx="13" cy="13" r="13" fill="#1b96d4"/></svg>
  <h2 class="abs" style="left:624px;top:1633px">Online</h2>
  <p class="abs copy" style="left:589px;top:1680px;width:525px">If you live too far to meet our instructors in person, you can study with us using Wavlo. Wavlo is free and easy to use (www.wavlo.com). Many of our students from around the world find this a reasonable option. When you study with one of our instructors using Wavlo, you will be communicating via two-way video conference. You get the same individual attention to your voice that our local students receive.</p>
  <a class="btn" style="left:589px;top:1833px;width:158px;height:42px">Get Started</a>
</section>

<section class="abs consult">
  <h2 class="abs" style="left:116px;top:93px">Free Consultation With Marcus</h2>
  <p class="abs copy" style="left:116px;top:140px;width:640px">Marcus Hale has openings for a free 15 minute consultation over the phone. If you have questions about your voice, click here to set up your time slot.</p>
  <a class="btn" style="left:116px;top:233px;width:158px;height:44px">Get Started</a>
  <div class="abs" style="left:762px;top:38px;width:257px;height:316px;background:linear-gradient(180deg,#eae8e6,#c29a80 35%,#1d1d1f 62%,#121214)" role="img" aria-label="Portrait photo of Marcus Hale in a black turtleneck"></div>
</section>

<section>
  <div class="media" style="left:87px;top:2420px;width:334px;height:215px;background:linear-gradient(160deg,#4b4f58,#1f2228 55%,#3a3f49)" role="img" aria-label="Video player preview for Tone Ascent lesson one"></div>
  <h2 class="abs" style="left:487px;top:2420px">Tone Ascent</h2>
  <p class="abs copy" style="left:487px;top:2465px;width:625px">Tone Ascent is a Video Series designed to give you all the techniques you need to fully develop your singing voice. With 30 videos, sixty audio workouts, and an eBook, the platform is the most advanced you'll find anywhere. Click here for more information.</p>
  <a class="btn" style="left:487px;top:2580px;width:158px;height:42px">Click Here</a>
</section>

<section class="abs testimonials" role="img" aria-label="Faint mosaic of student portrait photos behind the testimonials">
  <h2>Loved by thousands of people world wide</h2>
  <div class="abs avatar" role="img" aria-label="Photo of student Tobias"></div>
  <p class="abs quote">I am so happy to have met you! Before Tone Ascent, I had vocal problems that clouded my mind and made it zero fun to sing. Now I sing again and even have a weekly job as a speaker.</p>
  <div class="abs cite">- Tobias, Germany</div>
  <div class="abs dots"><i class="on"></i><i></i><i></i><i></i></div>
</section>

<footer class="abs footer">
  <div class="links">Terms and Conditions | Privacy Promise | FAQ's | Contact Us</div>
  <div class="legal">Copyright © 2013. All Rights Reserved.</div>
  <div class="social" aria-hidden="true"><i></i><i></i><i></i><i></i></div>
</footer>

</body>
</html>
```